Website design for Harlow based systematic hedge fund

We have run previous craftmosaic competitions to design our company logo, business cards and the styling of our presentation deck (see attached files).
As the final step we are looking to get a website designed that is thematically consistent with these existing elements of our branding.
You can find some of our competitors websites below:
https://www.quelmarsh.example/
https://www.fenloor.example/
https://www.pyvart.example/
https://www.dulvet.example/
https://www.orbelmfunds.example/
https://www.valtrigo.example/
https://www.meskilfunds.example/home
We would like to have a website that works well on both mobile devices and desktops. Either just as one page that can be scrolled down, with links at the top that skips to certain sections, or a few separate pages that can be navigated by a top menu.
It should look professional, we are not after lots of animations or unnecessary transitions, and in particular the website must be smooth to navigate. We would like to avoid having peoples of people, we are happy to make use of elements from the presentation (for example the style of the cover slide, or the section slides with the faded bridge in the background), or 'financial' style images.
We would like to have the following sections for now. For some of these some example text has been provided, final text may change but it will be of similar length. For the other sections we are happy to just have template text for now. At the moment we are mainly interested to see styles/layouts as words can be added easily afterwards:
1) We will need a disclaimer pop up the first time someone visits the site (see for example the meskilfunds example).
2) Top page - company name, then in larger text "Bringing AI and Statistical Inference to Financial Markets", and somewhere in smaller text "Harlow Vectors is a quantitative asset manager with the singular focus of delivering algorithmic strategies that work"
3) "About us" section: will describe us as a company, details our approach, company values, and explains the company logo.
Example text:
"We deliver consistent alpha across liquid markets through the application of proprietary IP in Bayesian inference, machine learning and artificial intelligence. We are a multi-disciplinary team founded by experienced finance professionals from premier institutions, leading academics from the Thornbury Stellar Unit at Ashmere College and world-class software engineers.
Our logo portrays a sillhoute of the lattice walkway at Ashmere College. Our unique scientific approach allows us to bridge cutting-edge mathematical research and computing expertise with financial knowledge to bring algorithmns that work to liquid markets"
4) Hiring section, detailing our culture, what we are looking for.
Example text:
"We are always looking for exceptional talent to join our entrepreneurial team. We are looking for individuals who are creative thinkers, can demonstrate analytical rigour and are passionate about the intersection of science, finance and technology.
We prioritise having a company culture that promotes sharing ideas in a safe, collaborative research environment. We make sure that every member of the team has the oppertunity to explore their own ideas through weekly 'innovation time', and ensure that everyone gets the support they need to continue to grow as individuals within the company."
5) A section for news/press releases
6) Contact us area at the bottom with office location and email. We will need to list 3 addresses for our Harlow, London and Singapore offices, along with a couple of contact emails or phone numbers
7) A client login button at the top that will take them to a different website (unrelated to this one).

```html
<!DOCTYPE html>
<html lang="en">
<head>
<meta charset="utf-8">
<title>Harlow Vectors — Website</title>
<link href="https://fonts.googleapis.com/css2?family=Lexend:wght@300;400;500&display=swap" rel="stylesheet">
<style>
:root{
  --canvas:#eef0f3;
  --blue:#5a8fd2;
  --blue-deep:#2c63a8;
  --navy:#0e3e6c;
  --ink:#2a4f86;
  --text:#4f6691;
  --dark-box:#17263b;
  --card-head:#e4e9f0;
  --lilac:#d0d6f2;
  --field:#dde8f7;
  --white:#ffffff;
}
*{box-sizing:border-box;margin:0;padding:0}
html,body{width:1200px;height:2984px;overflow:hidden}
body{background:var(--canvas);font-family:"Lexend",sans-serif;font-weight:300;color:var(--text);position:relative}
.a{position:absolute}
.page{position:absolute;background:var(--white);overflow:hidden}
.desktop{left:375px;top:74px;width:752px;height:2825px}
.mobile{left:77px;top:74px;width:226px;height:2825px}
.hero{left:0;top:0;width:100%;background:var(--blue);color:var(--white)}
.brand{font-weight:500;letter-spacing:.5px;color:var(--navy)}
.section-title{width:100%;text-align:center;font-weight:500;color:var(--ink)}
.section-sub{width:100%;text-align:center;color:var(--text)}
.photo{background:linear-gradient(160deg,#3a3040,#b08a60 55%,#e5c585)}
.photo.tree{background:linear-gradient(180deg,#5b8fb8,#c4b69a 55%,#3a3a30)}
.photo.field{background:linear-gradient(180deg,#2f4b3f,#5f7f5a 50%,#27402f)}
.avatar{border-radius:50%;border:2px solid var(--blue-deep);background:linear-gradient(160deg,#6f5a52,#c89a78)}
.btn-outline{background:rgba(255,255,255,.95);color:var(--blue)}
.field-box{background:var(--field);color:#9aa9c2}
.d-nav a{color:var(--white);font-size:9px;font-weight:500;margin-left:24px;text-decoration:none}
.d-card{background:var(--white);box-shadow:0 2px 8px rgba(30,50,90,.12)}
.d-card .head{height:33px;background:var(--card-head);position:relative}
.icon-sq{position:absolute;background:var(--blue);display:flex;align-items:center;justify-content:center}
.d-card .body{padding:10px 10px;font-size:8.5px;line-height:17.5px;color:var(--text)}
.d-card .label{color:var(--blue);font-weight:400}
.t-card{background:var(--lilac);text-align:center}
.t-card .quote{background:#e9ecf9;margin:0 10px;padding:8px 8px;font-size:8.5px;line-height:17px}
.news-meta{font-size:7px;color:var(--ink)}
.news-meta b{background:#dfe6f2;padding:1px 3px;font-weight:400}
.news-meta i{margin-left:6px;font-style:italic}
.page-btn{border:1px solid #a8b6cc;font-size:7px;text-align:center;color:var(--text);background:var(--white)}
.page-btn.on{background:var(--navy);border-color:var(--navy);color:var(--white)}
.faq-item{border-left:2px solid var(--navy);background:#f4f5f7;font-size:8.5px;color:var(--ink);padding-left:16px}
.contact-list b{font-weight:400;color:var(--ink)}
.footer{background:var(--navy);color:#c7d6ea}
.footer h4{color:var(--white);font-weight:500}
</style>
</head>
<body>

<!-- ============== MOBILE ============== -->
<div class="page mobile">
  <header class="a hero" style="height:178px">
    <div class="a brand" style="left:12px;top:7px;font-size:5px">HARLOW</div>
    <svg class="a" style="left:205px;top:7px" width="8" height="6" viewBox="0 0 8 6"><path d="M0 .5h8M0 3h8M0 5.5h8" stroke="#0e3e6c" stroke-width="1"/></svg>
    <div class="a" style="left:14px;top:26px;width:200px;font-size:10px;font-weight:500;line-height:12px">Bringing AI and Statistical Inference to Financial Markets</div>
    <div class="a" style="left:14px;top:52px;width:200px;font-size:4.5px;line-height:7px;opacity:.9">Harlow Vectors is a quantitative asset manager with the singular focus of delivering algorithmic strategies that work</div>
    <div class="a btn-outline" style="left:14px;top:102px;width:68px;height:14px;font-size:5px;line-height:14px;text-align:center">Get started</div>
  </header>

  <div class="a" style="left:14px;top:202px;font-size:8px;font-weight:500;color:var(--ink)">About Harlow</div>
  <p class="a" style="left:14px;top:214px;width:198px;font-size:4.4px;line-height:6.6px;text-align:justify">We deliver consistent alpha across liquid markets through the application of proprietary IP in Bayesian inference, machine learning and artificial intelligence. We are a multi-disciplinary team founded by experienced finance professionals from premier institutions, leading academics from the Thornbury Stellar Unit at Ashmere College and world-class software engineers. Our logo portrays a silhouette of the lattice walkway at Ashmere College. Our unique scientific approach allows us to bridge cutting-edge mathematical research and computing expertise with financial knowledge to bring algorithms that work to liquid markets.</p>

  <div class="a" style="left:14px;top:290px;font-size:6px;font-weight:500;color:var(--ink)">Join our team</div>
  <p class="a" style="left:14px;top:299px;width:198px;font-size:4.2px;line-height:6px;text-align:justify">We are always looking for creative thinkers with analytical rigour who love science, finance and technology. Weekly innovation time and real support help everyone grow.</p>

  <div class="a section-title" style="top:336px;font-size:8px">Our values</div>
  <div class="a section-sub" style="top:351px;font-size:4.5px">Lorem ipsum dolor sit amet consectetur adipisicing elit.</div>

  <div class="a d-card" style="left:51px;top:378px;width:124px;height:95px">
    <div class="head" style="height:20px"><div class="icon-sq" style="left:6px;top:4px;width:12px;height:12px"><svg width="7" height="6" viewBox="0 0 10 8"><path d="M2 0h6l2 3-5 5-5-5z" fill="none" stroke="#fff" stroke-width="1.2"/></svg></div></div>
    <div style="padding:5px 6px;font-size:4.5px;line-height:6.5px"><span style="color:var(--blue)">Reliability</span><br>Lorem ipsum dolor sit amet consectetur adipisicing elit. Magni hic placeat obcaecati nostrum odio perspiciatis ab animi consectetur ea facere.</div>
  </div>
  <div class="a d-card" style="left:51px;top:484px;width:124px;height:97px">
    <div class="head" style="height:20px"><div class="icon-sq" style="left:6px;top:4px;width:12px;height:12px"><svg width="7" height="6" viewBox="0 0 10 8"><path d="M2 0h6l2 3-5 5-5-5z" fill="none" stroke="#fff" stroke-width="1.2"/></svg></div></div>
    <div style="padding:5px 6px;font-size:4.5px;line-height:6.5px"><span style="color:var(--blue)">Reliability</span><br>Lorem ipsum dolor sit amet consectetur adipisicing elit. Magni hic placeat obcaecati nostrum odio perspiciatis ab animi consectetur ea facere.</div>
  </div>
  <div class="a d-card" style="left:51px;top:592px;width:124px;height:97px">
    <div class="head" style="height:20px"><div class="icon-sq" style="left:6px;top:4px;width:12px;height:12px"><svg width="7" height="6" viewBox="0 0 10 8"><path d="M2 0h6l2 3-5 5-5-5z" fill="none" stroke="#fff" stroke-width="1.2"/></svg></div></div>
    <div style="padding:5px 6px;font-size:4.5px;line-height:6.5px"><span style="color:var(--blue)">Reliability</span><br>Lorem ipsum dolor sit amet consectetur adipisicing elit. Magni hic placeat obcaecati nostrum odio perspiciatis ab animi consectetur ea facere.</div>
  </div>
  <div class="a d-card" style="left:51px;top:698px;width:124px;height:97px">
    <div class="head" style="height:20px"><div class="icon-sq" style="left:6px;top:4px;width:12px;height:12px"><svg width="7" height="6" viewBox="0 0 10 8"><path d="M2 0h6l2 3-5 5-5-5z" fill="none" stroke="#fff" stroke-width="1.2"/></svg></div></div>
    <div style="padding:5px 6px;font-size:4.5px;line-height:6.5px"><span style="color:var(--blue)">Reliability</span><br>Lorem ipsum dolor sit amet consectetur adipisicing elit. Magni hic placeat obcaecati nostrum odio perspiciatis ab animi consectetur ea facere.</div>
  </div>

  <section class="a" style="left:0;top:823px;width:226px;height:523px;background:var(--blue)">
    <div class="a section-title" style="top:18px;font-size:7px;color:var(--white)">Read what people talk about us</div>
    <div class="a section-sub" style="top:29px;font-size:4.5px;color:var(--white)">Lorem ipsum dolor sit amet consectetur adipisicing elit.</div>
    <div class="a t-card" style="left:51px;top:50px;width:124px;height:144px">
      <div class="a avatar" role="img" aria-label="Portrait photo of a client" style="left:39px;top:14px;width:46px;height:46px"></div>
      <div class="a" style="left:0;top:68px;width:124px;font-size:4.5px;line-height:6px"><span style="color:var(--blue)">Mara Jennet</span><br>United Kingdom, London</div>
      <div class="a" style="left:7px;top:92px;width:110px;background:#e9ecf9;font-size:4.5px;line-height:6.5px;padding:4px">Lorem ipsum dolor sit amet consectetur adipisicing elit. Minima cumque suscipit soluta et odio aperiam.</div>
    </div>
    <div class="a t-card" style="left:51px;top:202px;width:124px;height:144px">
      <div class="a avatar" role="img" aria-label="Portrait photo of a client" style="left:39px;top:14px;width:46px;height:46px;background:linear-gradient(160deg,#7a8fa3,#c8a48a)"></div>
      <div class="a" style="left:0;top:68px;width:124px;font-size:4.5px;line-height:6px"><span style="color:var(--blue)">Jon Dale</span><br>United Kingdom, London</div>
      <div class="a" style="left:7px;top:92px;width:110px;background:#e9ecf9;font-size:4.5px;line-height:6.5px;padding:4px">Lorem ipsum dolor sit amet consectetur adipisicing elit. Minima cumque suscipit soluta et odio aperiam.</div>
    </div>
    <div class="a t-card" style="left:51px;top:354px;width:124px;height:144px">
      <div class="a avatar" role="img" aria-label="Portrait photo of a client" style="left:39px;top:14px;width:46px;height:46px;background:linear-gradient(160deg,#3d4a66,#d7ab88)"></div>
      <div class="a" style="left:0;top:68px;width:124px;font-size:4.5px;line-height:6px"><span style="color:var(--blue)">Maisie Dawlen</span><br>United Kingdom, London</div>
      <div class="a" style="left:7px;top:92px;width:110px;background:#e9ecf9;font-size:4.5px;line-height:6.5px;padding:4px">Lorem ipsum dolor sit amet consectetur adipisicing elit. Minima cumque suscipit soluta et odio aperiam.</div>
    </div>
  </section>

  <div class="a section-title" style="top:1368px;font-size:7px">Latest news</div>
  <div class="a section-sub" style="top:1380px;font-size:4.5px">Lorem ipsum dolor sit amet consectetur adipisicing elit. Quam!</div>
  <div class="a photo" role="img" aria-label="News photo: smiling woman at an event" style="left:51px;top:1399px;width:124px;height:134px"></div>
  <div class="a" style="left:54px;top:1537px;width:118px;font-size:4.2px;line-height:6px"><span class="news-meta" style="font-size:4.2px"><b>31 August 2021</b><i>Admin</i></span><br>Lorem ipsum dolor sit amet consectetur adipisicing elit. Quos debitis recusandae nulla non sint molestiae nam.</div>
  <div class="a photo tree" role="img" aria-label="News photo: lone tree at sunset" style="left:51px;top:1590px;width:124px;height:134px"></div>
  <div class="a" style="left:54px;top:1728px;width:118px;font-size:4.2px;line-height:6px"><span class="news-meta" style="font-size:4.2px"><b>31 August 2021</b><i>Admin</i></span><br>Lorem ipsum dolor sit amet consectetur adipisicing elit. Quos debitis recusandae nulla non sint molestiae nam.</div>
  <div class="a photo field" role="img" aria-label="News photo: person walking through a green field" style="left:51px;top:1782px;width:124px;height:135px"></div>
  <div class="a" style="left:54px;top:1921px;width:118px;font-size:4.2px;line-height:6px"><span class="news-meta" style="font-size:4.2px"><b>31 August 2021</b><i>Admin</i></span><br>Lorem ipsum dolor sit amet consectetur adipisicing elit. Quos debitis recusandae nulla non sint molestiae nam.</div>

  <div class="a" style="left:14px;top:1993px;width:200px;height:10px">
    <div class="a page-btn" style="left:0;top:0;width:20px;height:10px;line-height:9px;font-size:4px">Prev</div>
    <div class="a page-btn on" style="left:30px;top:0;width:14px;height:10px;line-height:9px;font-size:4px">1</div>
    <div class="a page-btn" style="left:52px;top:0;width:14px;height:10px;line-height:9px;font-size:4px">2</div>
    <div class="a page-btn" style="left:74px;top:0;width:14px;height:10px;line-height:9px;font-size:4px">3</div>
    <div class="a page-btn" style="left:96px;top:0;width:14px;height:10px;line-height:9px;font-size:4px">4</div>
    <div class="a" style="left:115px;top:0;font-size:5px">…</div>
    <div class="a page-btn" style="left:126px;top:0;width:14px;height:10px;line-height:9px;font-size:4px">10</div>
    <div class="a page-btn" style="left:148px;top:0;width:20px;height:10px;line-height:9px;font-size:4px">Next</div>
  </div>

  <div class="a section-title" style="top:2044px;font-size:7px">Frequently asked questions</div>
  <div class="a section-sub" style="top:2056px;font-size:4.5px">Lorem ipsum dolor sit amet consectetur adipisicing elit. At?</div>
  <div class="a faq-item" style="left:14px;top:2070px;width:198px;height:58px;padding-left:8px;font-size:4.5px;line-height:6.5px;padding-top:5px">–&nbsp;&nbsp;First asked question<br><span style="display:block;margin-top:4px;padding-left:6px;color:var(--text)">Lorem ipsum dolor sit amet consectetur adipisicing elit. Voluptates molestias enim illo cumque recusandae numquam veniam.</span></div>
  <div class="a faq-item" style="left:14px;top:2138px;width:198px;height:17px;padding-left:8px;font-size:4.5px;line-height:17px">+&nbsp;&nbsp;Second asked question</div>
  <div class="a faq-item" style="left:14px;top:2166px;width:198px;height:17px;padding-left:8px;font-size:4.5px;line-height:17px">+&nbsp;&nbsp;Third asked question</div>
  <div class="a faq-item" style="left:14px;top:2196px;width:198px;height:58px;padding-left:8px;font-size:4.5px;line-height:6.5px;padding-top:5px">–&nbsp;&nbsp;Fourth asked question<br><span style="display:block;margin-top:4px;padding-left:6px;color:var(--text)">Lorem ipsum dolor sit amet consectetur adipisicing elit. Voluptates molestias enim illo cumque recusandae numquam veniam.</span></div>
  <div class="a faq-item" style="left:14px;top:2264px;width:198px;height:17px;padding-left:8px;font-size:4.5px;line-height:17px">+&nbsp;&nbsp;Fifth asked question</div>
  <div class="a faq-item" style="left:14px;top:2292px;width:198px;height:17px;padding-left:8px;font-size:4.5px;line-height:17px">+&nbsp;&nbsp;Sixth asked question</div>

  <div class="a section-title" style="top:2358px;font-size:7px">Get in touch</div>
  <div class="a section-sub" style="top:2370px;font-size:4.5px">Lorem ipsum dolor sit amet consectetur adipisicing elit. At?</div>
  <div class="a field-box" style="left:14px;top:2384px;width:198px;height:71px;font-size:4.2px;padding:4px">Enter message</div>
  <div class="a field-box" style="left:14px;top:2463px;width:198px;height:11px;font-size:4.2px;padding:3px 4px">Enter subject</div>
  <div class="a field-box" style="left:14px;top:2486px;width:198px;height:11px;font-size:4.2px;padding:3px 4px">Enter your name</div>
  <div class="a field-box" style="left:14px;top:2509px;width:198px;height:11px;font-size:4.2px;padding:3px 4px">Enter email address</div>
  <div class="a" style="left:14px;top:2530px;width:198px;height:12px;background:#e4e6ea;font-size:4.2px;line-height:12px;text-align:center">Send message</div>
  <div class="a contact-list" style="left:14px;top:2550px;width:198px;font-size:4.1px;line-height:5.4px">
    <div style="display:flex;gap:8px">
      <div style="width:95px"><b>Harlow, United Kingdom</b><br>Quayside Court 12</div>
      <div style="width:95px"><b>London, United Kingdom</b><br>Pellham Street 4</div>
    </div>
    <div style="display:flex;gap:8px;margin-top:4px">
      <div style="width:95px"><b>Singapore</b><br>Marlowe Road 18</div>
      <div style="width:95px"><b>0 1000 555 0199</b><br>Mon to Fri 8am to 5pm</div>
    </div>
    <div style="display:flex;gap:8px;margin-top:4px">
      <div style="width:95px"><b>info@harlowvectors.example</b><br>Send us your query</div>
      <div style="width:95px"><b>careers@harlowvectors.example</b><br>Join our team</div>
    </div>
  </div>

  <footer class="a footer" style="left:0;top:2638px;width:226px;height:187px;font-size:4.3px;line-height:6px">
    <div class="a" style="left:14px;top:12px;width:198px">
      <h4 style="font-size:5px">About Harlow</h4>
      <p>Lorem ipsum dolor sit amet consectetur adipisicing elit. Aperiam et, dolorum dignissimos voluptatibus quas repudiandae. Maxime laboriosam delectus commodi unde dolor.</p>
      <h4 style="font-size:5px;margin-top:3px">Navigation links</h4>
      <p style="color:#5f88c4">Home<br>FAQ<br>Contact us</p>
      <h4 style="font-size:5px;margin-top:3px">Newsletter</h4>
      <p>Lorem ipsum dolor sit amet consectetur adipisicing elit. Aperiam et, dolorum dignissimos voluptatibus quas repudiandae. Maxime laboriosam delectus commodi unde dolor.</p>
    </div>
    <div class="a" style="left:14px;top:134px;width:138px;height:10px;background:var(--white);color:#9aa9c2;font-size:4px;line-height:10px;padding-left:3px">Enter email address</div>
    <div class="a" style="left:155px;top:134px;width:50px;height:10px;background:#e4e6ea;color:var(--ink);font-size:4px;line-height:10px;text-align:center">Subscribe</div>
    <div class="a" style="left:0;top:164px;width:226px;text-align:center;font-size:4.3px">Copyright ©2021 All rights reserved</div>
  </footer>
</div>

<!-- ============== DESKTOP ============== -->
<div class="page desktop">
  <header class="a hero" style="height:378px">
    <div class="a brand" style="left:17px;top:12px;font-size:8px">HARLOW</div>
    <nav class="a d-nav" style="left:356px;top:15px;display:flex;align-items:center">
      <a href="#" style="border-bottom:1px solid #fff;padding-bottom:3px">Home</a><a href="#">About</a><a href="#">Values</a><a href="#">News</a><a href="#">FAQ</a><a href="#">Contact</a>
      <a href="#" style="background:#fff;color:var(--blue);border-radius:9px;padding:4px 12px;margin-left:26px">Login</a>
    </nav>
    <h1 class="a" style="left:70px;top:144px;font-size:22.5px;font-weight:500;letter-spacing:-.1px">Bringing AI and Statistical Inference to Financial Markets</h1>
    <p class="a" style="left:70px;top:185px;font-size:9.5px;opacity:.95">Harlow Vectors is a quantitative asset manager with the singular focus of delivering algorithmic strategies that work</p>
    <div class="a btn-outline" style="left:70px;top:244px;width:98px;height:23px;font-size:8px;line-height:23px;text-align:center">Get started</div>
  </header>

  <h2 class="a" style="left:70px;top:406px;font-size:12.5px;font-weight:500;color:var(--ink)">About Harlow</h2>
  <p class="a" style="left:70px;top:427px;width:256px;font-size:8.7px;line-height:17.6px;text-align:justify">We deliver consistent alpha across liquid markets through the application of proprietary IP in Bayesian inference, machine learning and artificial intelligence. We are a multi-disciplinary team founded by experienced finance professionals from premier institutions, leading academics from the Thornbury Stellar Unit at Ashmere College and world-class software engineers.<br>Our logo portrays a silhouette of the lattice walkway at Ashmere College. Our unique scientific approach allows us to bridge cutting-edge mathematical research and computing expertise with financial knowledge to bring algorithms that work to liquid markets.</p>
  <div class="a" role="img" aria-label="Company brand panel" style="left:350px;top:405px;width:307px;height:231px;background:var(--dark-box);display:flex;align-items:center;justify-content:center">
    <span style="font-size:13px;font-weight:400;color:var(--white)">Harlow Vectors</span>
  </div>

  <h2 class="a section-title" style="top:692px;font-size:12.5px">Our values</h2>
  <p class="a section-sub" style="top:715px;font-size:8.5px">Lorem ipsum dolor sit amet consectetur adipisicing elit.</p>

  <div class="a d-card" style="left:82px;top:769px;width:175px;height:175px">
    <div class="head"><div class="icon-sq" style="left:8px;top:7px;width:21px;height:19px"><svg width="10" height="8" viewBox="0 0 10 8"><path d="M2 0h6l2 3-5 5-5-5z" fill="none" stroke="#fff" stroke-width="1.2"/></svg></div></div>
    <div class="body"><span class="label">Reliability</span><br>Lorem ipsum dolor sit amet consectetur adipisicing elit. Magni hic placeat obcaecati nostrum odio perspiciatis ab animi consectetur ea facere.</div>
  </div>
  <div class="a d-card" style="left:288px;top:769px;width:175px;height:175px">
    <div class="head"><div class="icon-sq" style="left:8px;top:7px;width:21px;height:19px"><svg width="10" height="8" viewBox="0 0 10 8"><path d="M2 0h6l2 3-5 5-5-5z" fill="none" stroke="#fff" stroke-width="1.2"/></svg></div></div>
    <div class="body"><span class="label">Reliability</span><br>Lorem ipsum dolor sit amet consectetur adipisicing elit. Magni hic placeat obcaecati nostrum odio perspiciatis ab animi consectetur ea facere.</div>
  </div>
  <div class="a d-card" style="left:495px;top:769px;width:175px;height:175px">
    <div class="head"><div class="icon-sq" style="left:8px;top:7px;width:21px;height:19px"><svg width="10" height="8" viewBox="0 0 10 8"><path d="M2 0h6l2 3-5 5-5-5z" fill="none" stroke="#fff" stroke-width="1.2"/></svg></div></div>
    <div class="body"><span class="label">Reliability</span><br>Lorem ipsum dolor sit amet consectetur adipisicing elit. Magni hic placeat obcaecati nostrum odio perspiciatis ab animi consectetur ea facere.</div>
  </div>
  <div class="a d-card" style="left:82px;top:976px;width:175px;height:175px">
    <div class="head"><div class="icon-sq" style="left:8px;top:7px;width:21px;height:19px"><svg width="10" height="8" viewBox="0 0 10 8"><path d="M2 0h6l2 3-5 5-5-5z" fill="none" stroke="#fff" stroke-width="1.2"/></svg></div></div>
    <div class="body"><span class="label">Reliability</span><br>Lorem ipsum dolor sit amet consectetur adipisicing elit. Magni hic placeat obcaecati nostrum odio perspiciatis ab animi consectetur ea facere.</div>
  </div>

  <section class="a" style="left:290px;top:976px;width:380px;height:175px">
    <h2 style="font-size:12.5px;font-weight:500;color:var(--ink)">Join our team</h2>
    <p style="margin-top:6px;font-size:8.2px;line-height:14.5px;text-align:justify">We are always looking for exceptional talent to join our entrepreneurial team. We are looking for individuals who are creative thinkers, can demonstrate analytical rigour and are passionate about the intersection of science, finance and technology.</p>
    <p style="margin-top:5px;font-size:8.2px;line-height:14.5px;text-align:justify">We prioritise a culture that promotes sharing ideas in a safe, collaborative research environment. Every member of the team can explore their own ideas through weekly 'innovation time', with the support they need to keep growing within the company.</p>
  </section>

  <section class="a" style="left:0;top:1190px;width:752px;height:357px;background:var(--blue)">
    <h2 class="a section-title" style="top:30px;font-size:11.5px;color:var(--white)">Read what people talk about us</h2>
    <p class="a section-sub" style="top:51px;font-size:8.5px;color:var(--white)">Lorem ipsum dolor sit amet consectetur adipisicing elit.</p>
    <div class="a t-card" style="left:82px;top:77px;width:175px;height:242px">
      <div class="a avatar" role="img" aria-label="Portrait photo of a client" style="left:55px;top:20px;width:65px;height:65px"></div>
      <div class="a" style="left:0;top:95px;width:175px;font-size:8.5px;line-height:14px"><span style="color:var(--blue)">Mara Jennet</span><br>United Kingdom, London</div>
      <div class="a quote" style="left:0;top:140px;width:155px">Lorem ipsum dolor sit amet consectetur adipisicing elit. Minima cumque suscipit soluta et odio aperiam.</div>
    </div>
    <div class="a t-card" style="left:288px;top:77px;width:175px;height:242px">
      <div class="a avatar" role="img" aria-label="Portrait photo of a client" style="left:55px;top:20px;width:65px;height:65px;background:linear-gradient(160deg,#7a8fa3,#c8a48a)"></div>
      <div class="a" style="left:0;top:95px;width:175px;font-size:8.5px;line-height:14px"><span style="color:var(--blue)">Jon Dale</span><br>United Kingdom, London</div>
      <div class="a quote" style="left:0;top:140px;width:155px">Lorem ipsum dolor sit amet consectetur adipisicing elit. Minima cumque suscipit soluta et odio aperiam.</div>
    </div>
    <div class="a t-card" style="left:495px;top:77px;width:175px;height:242px">
      <div class="a avatar" role="img" aria-label="Portrait photo of a client" style="left:55px;top:20px;width:65px;height:65px;background:linear-gradient(160deg,#3d4a66,#d7ab88)"></div>
      <div class="a" style="left:0;top:95px;width:175px;font-size:8.5px;line-height:14px"><span style="color:var(--blue)">Maisie Dawlen</span><br>United Kingdom, London</div>
      <div class="a quote" style="left:0;top:140px;width:155px">Lorem ipsum dolor sit amet consectetur adipisicing elit. Minima cumque suscipit soluta et odio aperiam.</div>
    </div>
  </section>

  <h2 class="a section-title" style="top:1576px;font-size:12.5px">Latest news</h2>
  <p class="a section-sub" style="top:1598px;font-size:8.5px">Lorem ipsum dolor sit amet consectetur adipisicing elit. Quam!</p>
  <div class="a d-card" style="left:82px;top:1625px;width:175px;height:285px;box-shadow:0 1px 4px rgba(30,50,90,.08)">
    <div class="photo" role="img" aria-label="News photo: smiling woman at an event" style="height:192px"></div>
    <div style="padding:8px 6px;font-size:8.5px;line-height:17.5px"><div class="news-meta"><b>31 August 2021</b><i>Admin</i></div>Lorem ipsum dolor sit amet consectetur adipisicing elit. Quos debitis recusandae nulla non sint molestiae nam.</div>
  </div>
  <div class="a d-card" style="left:288px;top:1625px;width:175px;height:285px;box-shadow:0 1px 4px rgba(30,50,90,.08)">
    <div class="photo tree" role="img" aria-label="News photo: lone tree at sunset" style="height:192px"></div>
    <div style="padding:8px 6px;font-size:8.5px;line-height:17.5px"><div class="news-meta"><b>31 August 2021</b><i>Admin</i></div>Lorem ipsum dolor sit amet consectetur adipisicing elit. Quos debitis recusandae nulla non sint molestiae nam.</div>
  </div>
  <div class="a d-card" style="left:495px;top:1625px;width:175px;height:285px;box-shadow:0 1px 4px rgba(30,50,90,.08)">
    <div class="photo field" role="img" aria-label="News photo: person walking through a green field" style="height:192px"></div>
    <div style="padding:8px 6px;font-size:8.5px;line-height:17.5px"><div class="news-meta"><b>31 August 2021</b><i>Admin</i></div>Lorem ipsum dolor sit amet consectetur adipisicing elit. Quos debitis recusandae nulla non sint molestiae nam.</div>
  </div>

  <div class="a page-btn" style="left:178px;top:1962px;width:32px;height:16px;line-height:15px">Prev</div>
  <div class="a page-btn on" style="left:237px;top:1962px;width:26px;height:16px;line-height:15px">1</div>
  <div class="a page-btn" style="left:290px;top:1962px;width:26px;height:16px;line-height:15px">2</div>
  <div class="a page-btn" style="left:344px;top:1962px;width:26px;height:16px;line-height:15px">3</div>
  <div class="a page-btn" style="left:398px;top:1962px;width:26px;height:16px;line-height:15px">4</div>
  <div class="a" style="left:447px;top:1958px;font-size:10px">…</div>
  <div class="a page-btn" style="left:488px;top:1962px;width:26px;height:16px;line-height:15px">10</div>
  <div class="a page-btn" style="left:541px;top:1962px;width:32px;height:16px;line-height:15px">Next</div>

  <h2 class="a section-title" style="top:2035px;font-size:12.5px">Frequently asked questions</h2>
  <p class="a section-sub" style="top:2057px;font-size:8.5px">Lorem ipsum dolor sit amet consectetur adipisicing elit. At?</p>
  <div class="a faq-item" style="left:70px;top:2074px;width:304px;height:98px;padding-top:12px;line-height:17px">–&nbsp;&nbsp;&nbsp;First asked question<p style="margin:6px 0 0 18px;color:var(--text)">Lorem ipsum dolor sit amet consectetur adipisicing elit. Voluptates molestias enim illo cumque recusandae numquam veniam.</p></div>
  <div class="a faq-item" style="left:378px;top:2074px;width:304px;height:98px;padding-top:12px;line-height:17px">–&nbsp;&nbsp;&nbsp;Fourth asked question<p style="margin:6px 0 0 18px;color:var(--text)">Lorem ipsum dolor sit amet consectetur adipisicing elit. Voluptates molestias enim illo cumque recusandae numquam veniam.</p></div>
  <div class="a faq-item" style="left:70px;top:2183px;width:304px;height:32px;line-height:32px">+&nbsp;&nbsp;&nbsp;Second asked question</div>
  <div class="a faq-item" style="left:378px;top:2183px;width:304px;height:32px;line-height:32px;border-left-color:transparent">+&nbsp;&nbsp;&nbsp;Fifth asked question</div>
  <div class="a faq-item" style="left:70px;top:2225px;width:304px;height:32px;line-height:32px">+&nbsp;&nbsp;&nbsp;Third asked question</div>
  <div class="a faq-item" style="left:378px;top:2225px;width:304px;height:32px;line-height:32px;border-left-color:transparent">+&nbsp;&nbsp;&nbsp;Sixth asked question</div>

  <h2 class="a section-title" style="top:2321px;font-size:12.5px">Get in touch</h2>
  <p class="a section-sub" style="top:2344px;font-size:8.5px">Lorem ipsum dolor sit amet consectetur adipisicing elit. At?</p>
  <div class="a field-box" style="left:82px;top:2362px;width:333px;height:107px;font-size:7px;padding:6px 8px;border:1px solid #c8d6ec">Enter message</div>
  <div class="a field-box" style="left:82px;top:2481px;width:333px;height:21px;font-size:7px;line-height:21px;padding-left:8px">Enter subject</div>
  <div class="a field-box" style="left:82px;top:2514px;width:333px;height:21px;font-size:7px;line-height:21px;padding-left:8px">Enter your name</div>
  <div class="a field-box" style="left:82px;top:2547px;width:333px;height:21px;font-size:7px;line-height:21px;padding-left:8px">Enter email address</div>
  <div class="a" style="left:82px;top:2579px;width:333px;height:22px;background:#e4e6ea;font-size:7.5px;line-height:22px;text-align:center">Send message</div>

  <svg class="a" style="left:432px;top:2362px" width="10" height="240" viewBox="0 0 10 240">
    <g fill="none" stroke="#2c63a8" stroke-width="1">
      <path d="M5 11C2 7 2 2 5 2s3 5 0 9z"/>
      <path d="M5 51C2 47 2 42 5 42s3 5 0 9z"/>
      <path d="M5 91C2 87 2 82 5 82s3 5 0 9z"/>
      <path d="M1 123c2 5 5 7 7 7l1-2-2-1.5-1.2 1c-1.3-.8-2.3-1.8-3-3l1-1.2L2.5 121z"/>
      <rect x="1" y="163" width="8" height="6"/><path d="M1 163l4 3 4-3"/>
      <rect x="1" y="203" width="8" height="6"/><path d="M1 203l4 3 4-3"/>
    </g>
  </svg>
  <div class="a contact-list" style="left:450px;top:2360px;font-size:8px;line-height:12px">
    <div style="height:40px"><b>Harlow, United Kingdom</b><br>Quayside Court 12</div>
    <div style="height:40px"><b>London, United Kingdom</b><br>Pellham Street 4</div>
    <div style="height:40px"><b>Singapore</b><br>Marlowe Road 18</div>
    <div style="height:40px"><b>0 1000 555 0199</b><br>Mon to Fri 8am to 5pm</div>
    <div style="height:40px"><b>info@harlowvectors.example</b><br>Send us your query</div>
    <div style="height:40px"><b>careers@harlowvectors.example</b><br>Join our team</div>
  </div>

  <footer class="a footer" style="left:0;top:2633px;width:752px;height:192px;font-size:8.5px;line-height:17px">
    <div class="a" style="left:70px;top:22px;width:200px">
      <h4 style="font-size:9.5px;margin-bottom:6px">About Harlow</h4>
      <p>Lorem ipsum dolor sit amet consectetur adipisicing elit. Aperiam et, dolorum dignissimos voluptatibus quas repudiandae. Maxime laboriosam delectus commodi unde dolor.</p>
    </div>
    <div class="a" style="left:274px;top:22px;width:180px">
      <h4 style="font-size:9.5px;margin-bottom:6px">Navigation links</h4>
      <p style="color:#5f88c4;line-height:11px">Home<br>FAQ<br>Contact us</p>
    </div>
    <div class="a" style="left:478px;top:22px;width:206px">
      <h4 style="font-size:9.5px;margin-bottom:6px">Newsletter</h4>
      <p>Lorem ipsum dolor sit amet consectetur adipisicing elit. Aperiam et, dolorum dignissimos voluptatibus quas repudiandae. Maxime laboriosam delectus commodi unde dolor.</p>
      <div style="display:flex;margin-top:8px">
        <div style="width:140px;height:15px;background:#fff;color:#9aa9c2;font-size:6.5px;line-height:15px;padding-left:4px">Enter email address</div>
        <div style="width:48px;height:15px;margin-left:4px;background:#e4e6ea;color:var(--ink);font-size:6.5px;line-height:15px;text-align:center">Subscribe</div>
      </div>
    </div>
    <div class="a" style="left:0;top:160px;width:752px;text-align:center;font-size:8px">Copyright ©2021 All rights reserved</div>
  </footer>
</div>

</body>
</html>
```